Finish off design for Tool Retailer- One Page Brochure site

We have started work on our tool shop sit but need to to get finished. Just a One page WP that needs tidying up and made to look better and complete.
We also need to be able upload specials and monthly catalogs.
More info in the brief
Target Market(s)
Trades, mines, industiral
Coding
Coded - Design and coding required
Number of Pages Required
1 page
Font styles to use
Sans Serif
Requirements
Must have
- Please see brief
Nice to have
- Please see brief
Should not have
- Please see brief

```html
<!DOCTYPE html>
<html lang="en">
<head>
<meta charset="utf-8">
<title>Ridgeline Tools</title>
<link rel="stylesheet" href="https://fonts.googleapis.com/css2?family=Roboto+Condensed:wght@400;700&family=Roboto:wght@400;500;700&display=swap">
<style>
:root{
  --red:#c21d2c;
  --red-dark:#a51724;
  --black:#0b0b0b;
  --ink:#1d1d1d;
  --grey-bg:#efefef;
  --grey-band:#e6e6e6;
  --footer:#2e2e2e;
  --footer-deep:#1c1c1c;
  --white:#ffffff;
  --muted:#555;
  --star-off:#9a9a9a;
}
*{box-sizing:border-box;margin:0;padding:0}
html,body{width:1200px;height:3482px;overflow:hidden}
body{font-family:"Roboto",Arial,sans-serif;color:var(--ink);background:var(--white);position:relative}
section,header,footer,nav{position:absolute;left:0;width:1200px}
.abs{position:absolute}
.heading{font-family:"Roboto Condensed",Arial,sans-serif;font-weight:700;text-transform:uppercase}
.btn{position:absolute;background:var(--red);color:var(--white);font-weight:500;display:flex;align-items:center;justify-content:center}

/* top bar */
.topbar{top:0;height:97px;background:var(--red)}
.brand{left:140px;top:24px;display:flex;align-items:center;gap:12px;color:var(--white);font-family:"Roboto Condensed",sans-serif;font-weight:700;font-size:34px;text-transform:uppercase}
.brand-square{width:26px;height:26px;background:var(--white)}
.signup-label{left:727px;top:16px;color:var(--white);font-family:"Roboto Condensed",sans-serif;font-weight:700;font-size:21px}
.signup-input{left:727px;top:46px;width:278px;height:35px;background:var(--white);color:#999;font-size:11px;padding:11px 10px}
.signup-btn{left:1007px;top:46px;width:49px;height:35px;background:var(--black);font-size:14px;font-weight:700}

/* navigation */
.mainnav{top:97px;height:35px;background:var(--black);color:var(--white);font-size:14px}
.nav-item{top:0;height:35px;line-height:35px}
.nav-item.is-active{top:5px;height:25px;line-height:25px;background:var(--white);color:var(--red);padding:0 14px;left:144px}
.follow{left:889px;top:0;line-height:35px;font-size:14px}
.social{top:10px;width:15px;height:15px;background:var(--white);border-radius:2px}

/* hero */
.hero{top:132px;height:425px}
.hero-photo{position:absolute;inset:0;background:linear-gradient(90deg,#3c4650 0%,#5a5046 30%,#6c5f51 55%,#3b332b 100%)}
.hero-shade{position:absolute;inset:0;background:linear-gradient(90deg,rgba(0,0,0,0) 35%,rgba(0,0,0,.45) 100%)}
.hero-title{right:144px;top:66px;text-align:right;font-family:"Roboto Condensed",sans-serif;font-weight:700;font-size:62px;line-height:70px;text-transform:uppercase}
.hero-title .accent{color:var(--red)}
.hero-title .light{color:var(--white)}
.hero-text{right:144px;top:214px;width:540px;text-align:right;color:var(--white);font-size:17px;line-height:27px}
.hero-btn{left:877px;top:309px;width:179px;height:35px;font-size:17px}
.dots{left:560px;top:391px;display:flex;gap:10px}
.dots span{width:11px;height:11px;border-radius:50%;background:#bdbdbd}
.dots span.on{background:var(--white)}

/* features */
.features{top:557px;height:248px;background:var(--grey-bg)}
.feature{top:58px;width:286px;height:140px;background:var(--white);padding:16px 14px;border-radius:3px}
.feature h3{font-size:16px;font-weight:700;margin-bottom:10px}
.feature p{font-size:12px;line-height:16px;color:var(--muted)}
.feature.is-dark{background:var(--black)}
.feature.is-dark h3,.feature.is-dark p{color:var(--white)}

/* about */
.about{top:805px;height:523px;background:linear-gradient(90deg,#1a1a1a 0%,#242424 50%,#111 100%)}
.about h2{left:144px;top:100px;color:var(--white);font-size:30px}
.about-text{left:144px;top:160px;width:420px;color:#dcdcdc;font-size:13px;line-height:20px}
.about-text p+p{margin-top:8px}
.about-btn{left:144px;top:348px;width:101px;height:33px;font-size:13px;font-weight:700}
.about-photo{left:629px;top:98px;width:364px;height:327px;border:2px solid var(--white);background:linear-gradient(180deg,#9db6cf 0%,#c9d3db 38%,#8e6b5a 39%,#b49276 65%,#4c4c4c 70%,#5e5e5e 100%)}

/* product carousels */
.block-title{width:1200px;left:0;text-align:center;font-size:30px;color:var(--ink)}
.specials{top:1328px;height:552px;background:var(--grey-bg)}
.catalogue{top:2210px;height:494px;background:var(--grey-bg)}
.card{width:216px;background:var(--white);border-radius:3px;text-align:center}
.card-img{position:absolute;left:38px;width:140px;height:100px;border-radius:4px}
.card-name{position:absolute;left:0;width:100%;font-weight:700;font-size:15px}
.stars{position:absolute;left:0;width:100%;font-size:16px;color:var(--red);letter-spacing:3px}
.stars .off{color:var(--star-off)}
.arrow{width:16px;height:16px}
.cat-btn{left:14px;width:188px;height:33px;font-size:15px}

/* call to action */
.cta{top:1880px;height:330px;background:linear-gradient(90deg,#3a2e24 0%,#2b2b2b 45%,#3b3b3b 100%)}
.cta h2{left:0;width:1200px;text-align:center;top:68px;color:var(--white);font-size:34px}
.cta p{left:0;width:1200px;text-align:center;top:130px;color:var(--white);font-size:20px;line-height:36px}
.cta-btn{left:509px;top:216px;width:182px;height:34px;font-size:15px;font-weight:700}

/* partners */
.partners{top:2704px;height:302px;background:var(--grey-band)}
.partner{top:144px;width:172px;height:77px;background:var(--white);border:1px solid #d6d6d6;display:flex;align-items:center;justify-content:center}
.partner span{width:110px;height:26px;background:#cfcfcf;border-radius:3px}

/* newsletter band */
.newsletter{top:3006px;height:116px;background:var(--red);color:var(--white)}
.newsletter h2{left:237px;top:26px;font-family:"Roboto",sans-serif;font-weight:500;font-size:30px;text-transform:none}
.newsletter p{left:237px;top:66px;width:300px;font-size:12px;line-height:16px}
.nl-input{left:552px;top:37px;width:381px;height:42px;background:var(--white);color:#777;font-size:12px;padding:14px 12px}
.nl-btn{left:933px;top:37px;width:121px;height:42px;background:var(--black);font-size:15px;font-weight:700}

/* footer */
.site-footer{top:3122px;height:313px;background:var(--footer);color:var(--white)}
.footer-col h4{font-size:18px;font-weight:700;margin-bottom:18px}
.links li{list-style:none;font-size:13px;line-height:28px}
.links li::before{content:"›";margin-right:8px}
.contact-row{display:flex;gap:10px;font-size:12.5px;line-height:17px;margin-bottom:12px}
.contact-row b{display:block}
.divider{top:60px;width:1px;height:190px;background:#4a4a4a}
.inquiry{left:773px;top:18px;width:239px}
.inquiry h4{height:52px;background:var(--red);font-family:"Roboto Condensed",sans-serif;font-size:24px;display:flex;align-items:center;justify-content:center;text-transform:uppercase}
.field{margin-top:10px;height:33px;background:#e3e3e3;color:#555;font-size:12px;padding:9px 10px}
.field:first-of-type{margin-top:13px}
.submit{position:static;margin-top:9px;height:37px;font-size:18px}
.copyright{top:3435px;height:47px;background:var(--footer-deep);color:var(--white);font-size:12px}
</style>
</head>
<body>

<header class="topbar">
  <div class="abs brand"><span class="brand-square"></span>Ridgeline Tools</div>
  <div class="abs signup-label">NEWSLETTER SIGNUP</div>
  <div class="abs signup-input">Enter Your Email...</div>
  <div class="btn signup-btn">OK</div>
</header>

<nav class="mainnav">
  <div class="abs nav-item is-active">Home</div>
  <div class="abs nav-item" style="left:265px">About Us</div>
  <div class="abs nav-item" style="left:383px">Specials</div>
  <div class="abs nav-item" style="left:504px">Contact Us</div>
  <div class="abs nav-item" style="left:636px">Current Catalogue</div>
  <div class="abs follow">Follow Us On</div>
  <span class="abs social" style="left:984px"></span>
  <span class="abs social" style="left:1012px"></span>
  <span class="abs social" style="left:1040px"></span>
</nav>

<section class="hero">
  <div class="hero-photo" role="img" aria-label="Tradesman in hard hat drilling into a wall with a rotary hammer, dust flying"></div>
  <div class="hero-shade"></div>
  <h1 class="abs hero-title"><span class="accent">All Tools.</span><br><span class="light">For Any Occasion.</span></h1>
  <p class="abs hero-text">Mauris laoreet porta volutpat. Pellentesque ut elementum mattis. Aliquam imperdiet mattis diam, a blandit est elementum ut eu viverra lectus pellentesque tempus.</p>
  <div class="btn hero-btn">Contact Us Today</div>
  <div class="abs dots"><span class="on"></span><span></span><span></span></div>
</section>

<section class="features">
  <div class="abs feature" style="left:144px"><h3>Incredible Design &amp; Functionality</h3><p>Lorem ipsum dolor sit amet, consectetuer adipiscing elit, sed diam nonummy nibh euismod tincidunt ut laoreet dolore magna aliquam erat volutpat.</p></div>
  <div class="abs feature is-dark" style="left:455px"><h3>Awesome Look On Every Devices</h3><p>Lorem ipsum dolor sit amet, consectetuer adipiscing elit, sed diam nonummy nibh euismod tincidunt ut laoreet dolore magna aliquam erat volutpat.</p></div>
  <div class="abs feature" style="left:770px"><h3>Free Support &amp; Updates.</h3><p>Lorem ipsum dolor sit amet, consectetuer adipiscing elit, sed diam nonummy nibh euismod tincidunt ut laoreet dolore magna aliquam erat volutpat.</p></div>
</section>

<section class="about">
  <h2 class="abs heading">About Ridgeline Tools</h2>
  <div class="abs about-text">
    <p>Lorem ipsum dolor sit amet, consectetuer adipiscing elit, sed lord diam nonummy nibh euismod tincidunt ut laoreet dolore magnaas aliquam erat volutpat. Ut wisi enim ad minim veniam, quis nostrud exerci tation ullamcorper suscipit lobortis nisl ut.</p>
    <p>Etiam lacinia feugiat nibh eu malesuada. Mauris diam lorem,west cursus non nibh eget, laoreet molestie nibh. Ut at imperdiet ermi neque. Vestibulum lobortis scelerisque ipsum.</p>
  </div>
  <div class="btn about-btn">READ MORE</div>
  <div class="abs about-photo" role="img" aria-label="Street view of the tool shop storefront with a parked ute"></div>
</section>

<section class="specials">
  <h2 class="abs heading block-title" style="top:80px">Current Specials</h2>
  <svg class="abs arrow" style="left:86px;top:294px" viewBox="0 0 16 16"><path d="M10 3 5 8l5 5" fill="none" stroke="#222" stroke-width="2"/></svg>
  <svg class="abs arrow" style="left:1100px;top:294px" viewBox="0 0 16 16"><path d="M6 3l5 5-5 5" fill="none" stroke="#222" stroke-width="2"/></svg>
  <div class="abs card" style="left:142px;top:153px;height:297px">
    <div class="card-img" style="top:30px;background:linear-gradient(135deg,#c83a3a,#2a2a2a)" role="img" aria-label="Cordless drill twin pack"></div>
    <div class="card-name" style="top:213px">PRODUCT NAME 1</div>
    <div class="stars" style="top:238px">★★★<span class="off">★★</span></div>
  </div>
  <div class="abs card" style="left:374px;top:153px;height:297px">
    <div class="card-img" style="top:30px;background:linear-gradient(135deg,#4a86b5,#bfc4c8)" role="img" aria-label="Circular saw"></div>
    <div class="card-name" style="top:213px">PRODUCT NAME 2</div>
    <div class="stars" style="top:238px">★★★<span class="off">★★</span></div>
  </div>
  <div class="abs card" style="left:603px;top:153px;height:297px">
    <div class="card-img" style="top:30px;background:linear-gradient(135deg,#3f8a3f,#5a5a5a)" role="img" aria-label="Angle grinder"></div>
    <div class="card-name" style="top:211px">PRODUCT NAME 3</div>
    <div class="stars" style="top:236px">★★★★<span class="off">★</span></div>
  </div>
  <div class="abs card" style="left:838px;top:153px;height:297px">
    <div class="card-img" style="top:30px;background:linear-gradient(135deg,#4a86b5,#bfc4c8)" role="img" aria-label="Circular saw"></div>
    <div class="card-name" style="top:213px">PRODUCT NAME 4</div>
    <div class="stars" style="top:238px">★★★<span class="off">★★</span></div>
  </div>
</section>

<section class="cta">
  <div class="abs" style="inset:0;background:linear-gradient(90deg,rgba(80,60,40,.6),rgba(20,20,20,.4) 60%,rgba(60,60,60,.5))" role="img" aria-label="Hands operating a nail gun on timber framing"></div>
  <h2 class="abs heading">Lorem ipsum dolor sit amet, consectetuer</h2>
  <p class="abs">Adipiscing elit, aa sed diam nonummy nibh euismod tincidunt ut laoreet dolore magna<br>aliquam erat volutpat. Ut wisi enim ad minim veniam, quis nostrud exercitation.</p>
  <div class="btn cta-btn">CONTACT US TODAY</div>
</section>

<section class="catalogue">
  <h2 class="abs heading block-title" style="top:64px">Latest Catalogue</h2>
  <svg class="abs arrow" style="left:86px;top:289px" viewBox="0 0 16 16"><path d="M10 3 5 8l5 5" fill="none" stroke="#222" stroke-width="2"/></svg>
  <svg class="abs arrow" style="left:1100px;top:289px" viewBox="0 0 16 16"><path d="M6 3l5 5-5 5" fill="none" stroke="#222" stroke-width="2"/></svg>
  <div class="abs card" style="left:142px;top:148px;height:265px">
    <div class="card-img" style="top:26px;background:linear-gradient(135deg,#c83a3a,#2a2a2a)" role="img" aria-label="Cordless drill kit"></div>
    <div class="card-name" style="top:175px;font-weight:500;font-size:16px">Product 1</div>
    <div class="btn cat-btn" style="top:216px">Download Catalogue</div>
  </div>
  <div class="abs card" style="left:374px;top:148px;height:265px">
    <div class="card-img" style="top:26px;background:linear-gradient(135deg,#e8b923,#222)" role="img" aria-label="Drill kit with carry bag"></div>
    <div class="card-name" style="top:175px;font-weight:500;font-size:16px">Product 2</div>
    <div class="btn cat-btn" style="top:216px">Download Catalogue</div>
  </div>
  <div class="abs card" style="left:603px;top:148px;height:265px">
    <div class="card-img" style="top:26px;background:linear-gradient(135deg,#4a86b5,#bfc4c8)" role="img" aria-label="Circular saw"></div>
    <div class="card-name" style="top:175px;font-weight:500;font-size:16px">Product 3</div>
    <div class="btn cat-btn" style="top:216px">Download Catalogue</div>
  </div>
  <div class="abs card" style="left:838px;top:148px;height:265px">
    <div class="card-img" style="top:26px;background:linear-gradient(135deg,#e8b923,#222)" role="img" aria-label="Drill kit with carry bag"></div>
    <div class="card-name" style="top:175px;font-weight:500;font-size:16px">Product 4</div>
    <div class="btn cat-btn" style="top:216px">Download Catalogue</div>
  </div>
</section>

<section class="partners">
  <h2 class="abs heading block-title" style="top:74px">Our Partners</h2>
  <svg class="abs arrow" style="left:86px;top:178px" viewBox="0 0 16 16"><path d="M10 3 5 8l5 5" fill="none" stroke="#999" stroke-width="2"/></svg>
  <svg class="abs arrow" style="left:1100px;top:178px" viewBox="0 0 16 16"><path d="M6 3l5 5-5 5" fill="none" stroke="#333" stroke-width="2"/></svg>
  <div class="abs partner" style="left:144px"><span></span></div>
  <div class="abs partner" style="left:330px"><span></span></div>
  <div class="abs partner" style="left:515px"><span></span></div>
  <div class="abs partner" style="left:701px"><span></span></div>
  <div class="abs partner" style="left:886px"><span></span></div>
</section>

<section class="newsletter">
  <svg class="abs" style="left:142px;top:34px" width="72" height="46" viewBox="0 0 72 46"><g fill="none" stroke="#fff" stroke-width="2.5"><rect x="24" y="6" width="44" height="34"/><path d="M24 6l22 18L68 6"/><path d="M4 14h14M8 22h10M2 30h16"/></g></svg>
  <h2 class="abs">Newsletter</h2>
  <p class="abs">Get the latest news on new arrivals, gifts special offers and other discount information.</p>
  <div class="abs nl-input">Enter Your Email...</div>
  <div class="btn nl-btn">SUBSCRIBE</div>
</section>

<footer class="site-footer">
  <div class="abs footer-col" style="left:144px;top:52px">
    <h4>Quick Links</h4>
    <ul class="links"><li>Home</li><li>About Us</li><li>Specials</li><li>Contact Us</li><li>Current Catalogue</li></ul>
  </div>
  <div class="abs divider" style="left:343px"></div>
  <div class="abs footer-col" style="left:429px;top:52px;width:250px">
    <h4>Contact Details</h4>
    <div class="contact-row"><svg width="12" height="14" viewBox="0 0 12 14"><path d="M6 0a5 5 0 0 1 5 5c0 4-5 9-5 9S1 9 1 5a5 5 0 0 1 5-5z" fill="#fff"/><circle cx="6" cy="5" r="2" fill="#2e2e2e"/></svg><div><b>Ridgeline Tools</b>48 Quarry Road, Ironbark Plaza,<br>Unit 3, Emerald</div></div>
    <div class="contact-row"><svg width="12" height="14" viewBox="0 0 12 14"><path d="M2 1l3 0 1 3-2 1.5a8 8 0 0 0 3.5 3.5L9 7l3 1v3c0 1-1 2-2 2C5 13 0 8 0 3c0-1 1-2 2-2z" fill="#fff"/></svg><div><b>Phone</b>+61 7 5550 1234 / 88</div></div>
    <div class="contact-row"><svg width="12" height="14" viewBox="0 0 12 14"><rect x="0" y="3" width="12" height="9" fill="#fff"/><path d="M0 3l6 5 6-5" fill="none" stroke="#2e2e2e" stroke-width="1.2"/></svg><div><b>Email</b>hello@ridgelinetools.example</div></div>
  </div>
  <div class="abs divider" style="left:720px"></div>
  <div class="abs inquiry">
    <h4>Quick Inquiry</h4>
    <div class="field">Name</div>
    <div class="field">Phone</div>
    <div class="field">Email</div>
    <div class="field">Message</div>
    <div class="btn submit">Submit Now</div>
  </div>
</footer>

<div class="abs copyright" style="left:0;width:1200px">
  <span class="abs" style="left:144px;top:16px">Copyright © 2018 Ridgeline Tools. All Rights Reserved.</span>
  <span class="abs social" style="left:994px;top:15px"></span>
  <span class="abs social" style="left:1016px;top:15px"></span>
  <span class="abs social" style="left:1038px;top:15px"></span>
</div>

</body>
</html>
```